Peter Lasko-Wren Finance

Need a personal website advertising Equipment Finance,Business Finance,Commercial Finance, Construction Finance, Bridging Finance. Similar websites are www.varoplend.com.au / www.kitmoxa.com.au / www.rzb4.com.au /wwwbelvaxcredit.com.au

Target Market(s)

Business People

Industry/Entity Type

Business

Number of Pages Required

3 page

Font styles to use
Serif
Sans Serif

Requirements
Must have
• All i want is a simple corporate looking website advertising Equipment Finance, Commercial Finance, Construction Finance, Business Finance, Bridging Finance,

```html
<!DOCTYPE html>
<html lang="en">
<head>
<meta charset="utf-8">
<title>Peter Lasko-Wren Finance</title>
<link href="https://fonts.googleapis.com/css2?family=Roboto:ital,wght@0,300;0,400;0,500;0,700;1,400&family=Lato:wght@400;700&display=swap" rel="stylesheet">
<style>
:root{
  --blue:#0f9edc;
  --blue-dark:#0b86c0;
  --green:#b9d12c;
  --grey:#6d7073;
  --text:#4a4d50;
  --light:#f5f5f5;
  --footer:#24262d;
  --footer-text:#c9cbd0;
  --white:#ffffff;
}
*{margin:0;padding:0;box-sizing:border-box}
html,body{width:1200px;height:3186px;overflow:hidden;background:var(--white)}
body{position:relative;font-family:"Roboto",Arial,sans-serif;color:var(--text)}
.abs{position:absolute}

/* header */
.top-strip{left:0;top:0;width:1200px;height:9px;background:#5d6064}
.site-header{left:0;top:9px;width:1200px;height:119px;background:var(--white)}
.brand{left:90px;top:34px;display:flex;align-items:center;gap:12px;font-family:"Lato",Arial,sans-serif;font-weight:700;font-size:30px;color:var(--grey);white-space:nowrap}
.brand .dot{width:14px;height:14px;border-radius:50%;background:var(--green)}
.contact{top:33px;display:flex;align-items:center;gap:14px;font-size:19px;color:var(--grey)}
.contact .icon{width:52px;height:52px;border-radius:50%;background:var(--green);display:flex;align-items:center;justify-content:center}
.contact.phone{left:500px;letter-spacing:1px}
.contact.mail{left:708px;font-size:15px}
.socials{display:flex;gap:6px}
.socials span{width:22px;height:22px;border-radius:50%;background:var(--grey);display:block}
.header-socials{left:974px;top:48px}

.main-nav{left:0;top:128px;width:1200px;height:42px;background:var(--blue);display:flex;justify-content:center;padding-left:0}
.main-nav ul{list-style:none;display:flex;margin-left:-12px}
.main-nav li{font-size:15px;color:var(--white);line-height:42px;padding:0 12px}
.main-nav li.active{background:var(--green);color:var(--grey)}

/* hero */
.hero{left:0;top:170px;width:1200px;height:690px;overflow:hidden}
.hero-photo{position:absolute;inset:0;background:radial-gradient(ellipse at 80% 40%,#b8bec6 0%,#7c858f 30%,#2e3d52 62%,#0f1a2b 100%)}
.hero-title{left:87px;top:150px;font-size:43px;font-weight:500;line-height:50px;color:var(--white);letter-spacing:1.5px}
.hero-sub{left:88px;top:268px;font-size:15px;font-weight:500;line-height:18px;color:var(--white)}
.btn-quote{left:87px;top:340px;width:265px;height:72px;border:2px solid var(--white);color:var(--white);font-size:21px;font-weight:500;letter-spacing:2px;display:flex;align-items:center;justify-content:center}
.slider-dots{left:992px;top:604px;display:flex;gap:4px}
.slider-dots span{width:17px;height:17px;border:2px solid var(--white);border-radius:50%}
.slider-dots span.on{background:var(--white);box-shadow:inset 0 0 0 3px #8a9098}

/* services */
.services{left:0;top:850px;width:1200px;height:881px;background:var(--light)}
.services-bg{position:absolute;inset:0}
.card{width:255px;height:357px;background:var(--white);box-shadow:0 2px 6px rgba(0,0,0,.18)}
.card-media{height:153px;background:linear-gradient(135deg,#c9cf4e,#8f9a2e);position:relative;border-left:16px solid #6a6d69}
.card-media h3{position:absolute;left:8px;top:14px;font-size:30px;font-weight:700;line-height:37px;color:var(--white);letter-spacing:.5px}
.card p{font-size:15px;font-style:italic;line-height:20px;color:var(--grey);text-align:center;padding:28px 24px 0;letter-spacing:.5px}
.card .btn-more{position:absolute;left:50%;transform:translateX(-50%);top:295px;width:148px;height:36px;background:var(--blue);color:var(--white);font-size:13px;font-weight:500;letter-spacing:1px;display:flex;align-items:center;justify-content:center}

/* about */
.about-title{left:121px;top:1757px;font-size:26px;font-weight:500;letter-spacing:1.5px;color:#2f3235}
.about-photo{left:121px;top:1820px;width:368px;height:512px;background:linear-gradient(160deg,#e9dfdc 0%,#cfc8c6 40%,#4b4d50 75%,#2a2b2e 100%)}
.about-text{left:537px;top:1828px;width:540px;font-size:12px;line-height:14px;color:var(--grey)}
.checklist{left:573px;top:1943px;list-style:none;width:520px}
.checklist li{position:relative;padding-left:62px;font-size:16px;line-height:38px;letter-spacing:.6px;color:var(--text)}
.checklist li svg{position:absolute;left:0;top:14px}
.badges{left:634px;top:2255px;display:flex;align-items:center;gap:50px}
.badge{border-radius:4px}

/* testimonials */
.testimonials{left:0;top:2400px;width:1200px;height:361px;background:var(--blue)}
.testimonials h2{position:absolute;left:118px;top:24px;font-size:27px;font-weight:500;letter-spacing:1.5px;color:var(--white)}
.avatar{left:211px;top:74px;width:220px;height:220px;border-radius:50%;border:5px solid var(--green);background:radial-gradient(circle at 50% 40%,#c9a48c,#8a6a58 70%,#5c4a40)}
.reviewer{left:211px;top:305px;width:220px;text-align:center;font-size:21px;font-weight:500;letter-spacing:1px;color:var(--white)}
.stars{left:860px;top:68px;display:flex;gap:2px}
.quote{left:478px;top:118px;width:600px;font-size:18px;line-height:43px;letter-spacing:.6px;color:var(--white)}
.arrow{top:164px}

/* footer */
.site-footer{left:0;top:2761px;width:1200px;height:425px;background:var(--footer);color:var(--footer-text)}
.footer-brand{left:78px;top:42px;font-family:"Lato",Arial,sans-serif;font-weight:700;font-size:28px;color:var(--white);white-space:nowrap}
.footer-about{left:78px;top:124px;width:300px;font-size:14px;line-height:17px;text-align:center;color:#a9acb2}
.footer-contact{left:100px;list-style:none;font-size:15px;color:var(--white);letter-spacing:.5px}
.footer-contact li{display:flex;align-items:center;gap:16px;line-height:29px}
.footer-col{top:42px;list-style:none}
.footer-col h4{font-size:16px;font-weight:700;letter-spacing:1.5px;color:var(--white);margin-bottom:24px}
.footer-col li{font-size:16px;line-height:40px;letter-spacing:.6px}
.copyright{left:90px;top:364px;font-size:16px;letter-spacing:.6px;color:var(--footer-text)}
.copyright a{color:var(--footer-text)}
.footer-socials{left:896px;top:360px;gap:9px}
.footer-socials span{width:30px;height:30px;background:#6b6e74}
</style>
</head>
<body>

<div class="abs top-strip"></div>
<header class="abs site-header">
  <div class="abs brand"><span class="dot"></span>Peter Lasko-Wren Finance</div>
  <div class="abs contact phone">
    <span class="icon"><svg width="24" height="24" viewBox="0 0 24 24"><path fill="#fff" d="M6.6 10.8c1.4 2.8 3.8 5.1 6.6 6.6l2.2-2.2c.3-.3.7-.4 1-.2 1.1.4 2.3.6 3.6.6.6 0 1 .4 1 1V20c0 .6-.4 1-1 1C10.6 21 3 13.4 3 4c0-.6.4-1 1-1h3.5c.6 0 1 .4 1 1 0 1.3.2 2.5.6 3.6.1.3 0 .7-.2 1z"/></svg></span>
    904 318 277
  </div>
  <div class="abs contact mail">
    <span class="icon"><svg width="24" height="18" viewBox="0 0 24 18"><rect x="1" y="1" width="22" height="16" rx="2" fill="#fff"/><path d="M2 2l10 8 10-8" stroke="#b9d12c" stroke-width="2" fill="none"/></svg></span>
    info@laskowren.com
  </div>
  <div class="abs socials header-socials"><span></span><span></span><span></span><span></span><span></span></div>
</header>

<nav class="abs main-nav">
  <ul>
    <li class="active">Equipment Finance</li>
    <li>Business Finance</li>
    <li>Commercial Finance</li>
    <li>Construction Finance</li>
    <li>Bridging Finance</li>
  </ul>
</nav>

<section class="abs hero">
  <div class="hero-photo" role="img" aria-label="Blurred stock market chart on a trading screen"></div>
  <h1 class="abs hero-title">Financial Solutions that make<br>real business sense</h1>
  <p class="abs hero-sub">Lorem ipsum dolor sit amet, consectetur adipisicing elit,<br>sed do eiusmod tempor in.</p>
  <div class="abs btn-quote">GET A QUOTE</div>
  <div class="abs slider-dots"><span></span><span class="on"></span><span></span><span></span></div>
</section>

<section class="abs services">
  <svg class="services-bg" width="1200" height="881" viewBox="0 0 1200 881">
    <rect width="1200" height="881" fill="#f6f6f6"/>
    <path d="M0 0 L1200 0 L1200 60 C900 120 600 80 300 80 C180 80 80 60 0 40 Z" fill="#0f9edc" transform="translate(0,-80)"/>
    <path d="M0 10 C200 -20 500 -10 700 80 C900 170 1050 260 1200 330 L1200 380 C1050 320 900 240 700 160 C500 80 250 60 0 90 Z" fill="#b9d12c"/>
    <path d="M0 0 L1200 0 L1200 300 C1050 240 900 160 700 80 C500 0 200 -10 0 20 Z" fill="#0f9edc"/>
  </svg>
  <article class="abs card" style="left:121px;top:14px">
    <div class="card-media" role="img" aria-label="Financial charts and a calculator"><h3>Equipment<br>Finance</h3></div>
    <p>Lorem ipsum dolor sit amet, consectetur adipisicing elit, sed do.</p>
    <div class="btn-more">LEARN MORE</div>
  </article>
  <article class="abs card" style="left:461px;top:14px">
    <div class="card-media" role="img" aria-label="Business newspaper pages"><h3>Business<br>Finance</h3></div>
    <p>Lorem ipsum dolor sit amet, consectetur adipisicing elit, sed do.</p>
    <div class="btn-more">LEARN MORE</div>
  </article>
  <article class="abs card" style="left:822px;top:14px">
    <div class="card-media" role="img" aria-label="Hand writing on a financial report"><h3>Commercial<br>Finance</h3></div>
    <p>Lorem ipsum dolor sit amet, consectetur adipisicing elit, sed do.</p>
    <div class="btn-more">LEARN MORE</div>
  </article>
  <article class="abs card" style="left:312px;top:433px">
    <div class="card-media" role="img" aria-label="Small model house on stacked coins"><h3>Construction<br>Finance</h3></div>
    <p>Lorem ipsum dolor sit amet, consectetur adipisicing elit, sed do.</p>
    <div class="btn-more">LEARN MORE</div>
  </article>
  <article class="abs card" style="left:663px;top:433px">
    <div class="card-media" role="img" aria-label="Clock beside a pile of coins"><h3>Bridging<br>Finance</h3></div>
    <p>Lorem ipsum dolor sit amet, consectetur adipisicing elit, sed do.</p>
    <div class="btn-more">LEARN MORE</div>
  </article>
</section>

<section>
  <h2 class="abs about-title">GIVING BUSINESS THE FINANCIAL SUPPORT IT NEEDS TO GROW</h2>
  <div class="abs about-photo" role="img" aria-label="Modern glass office building against the sky"></div>
  <p class="abs about-text">Lorem ipsum dolor sit amet, consectetur adipisicing elit, sed do eiusmod tempor incididunt ut labore et dolore magna aliqua. Ut enim ad minim veniam, quis nostrud exercitation ullamco laboris nisi ut aliquip ex ea commodo consequat. Duis aute irure dolor in reprehenderit in voluptate velit esse cillum dolore eu fugiat nulla pariatur.</p>
  <ul class="abs checklist">
    <li><svg width="18" height="14" viewBox="0 0 18 14"><path d="M1 7l5 5L17 1" stroke="#b9d12c" stroke-width="3" fill="none"/></svg>Highly competitive rates from some of Australia's best known lenders</li>
    <li><svg width="18" height="14" viewBox="0 0 18 14"><path d="M1 7l5 5L17 1" stroke="#b9d12c" stroke-width="3" fill="none"/></svg>Professional service from an experienced team</li>
    <li><svg width="18" height="14" viewBox="0 0 18 14"><path d="M1 7l5 5L17 1" stroke="#b9d12c" stroke-width="3" fill="none"/></svg>Loan structures to suit your individual needs</li>
    <li><svg width="18" height="14" viewBox="0 0 18 14"><path d="M1 7l5 5L17 1" stroke="#b9d12c" stroke-width="3" fill="none"/></svg>Taking the hassle out of arranging finance</li>
    <li><svg width="18" height="14" viewBox="0 0 18 14"><path d="M1 7l5 5L17 1" stroke="#b9d12c" stroke-width="3" fill="none"/></svg>Help you every step of the process from pre-approval to settlement and beyond</li>
  </ul>
  <div class="abs badges">
    <div class="badge" style="width:100px;height:44px;background:#b9d12c"></div>
    <div class="badge" style="width:162px;height:44px;background:#c8cacc"></div>
    <div class="badge" style="width:80px;height:80px;border-radius:50%;background:#d7c9c2"></div>
  </div>
</section>

<section class="abs testimonials">
  <h2>SEE WHAT PEOPLE SAY ABOUT US</h2>
  <div class="abs avatar" role="img" aria-label="Portrait photo of the reviewer"></div>
  <div class="abs reviewer">Miles Corbett</div>
  <div class="abs stars">
    <svg width="160" height="32" viewBox="0 0 160 32">
      <g fill="#d9e436">
        <path id="star" d="M16 1l4.6 9.6 10.4 1.4-7.6 7.3 1.9 10.4L16 24.7l-9.3 5 1.9-10.4L1 12l10.4-1.4z"/>
        <use href="#star" x="32"/><use href="#star" x="64"/><use href="#star" x="96"/><use href="#star" x="128"/>
      </g>
    </svg>
  </div>
  <p class="abs quote">" True professional, very helpful and dedicated<br>What a company, an absolutely fabulous way to secure funds<br>for a new purchase,&nbsp; done quickly and perfect "</p>
  <svg class="abs arrow" style="left:92px" width="28" height="40" viewBox="0 0 28 40"><path d="M24 4L8 20l16 16" stroke="#fff" stroke-width="7" fill="none"/></svg>
  <svg class="abs arrow" style="left:1080px" width="28" height="40" viewBox="0 0 28 40"><path d="M4 4l16 16L4 36" stroke="#fff" stroke-width="7" fill="none"/></svg>
</section>

<footer class="abs site-footer">
  <div class="abs footer-brand">Peter Lasko-Wren Finance</div>
  <p class="abs footer-about">Proudly producing from the<br>New Brunswick, Nova Scotia,<br>Prince Edward Island, Canada.</p>
  <ul class="abs footer-contact" style="top:210px">
    <li><svg width="16" height="16" viewBox="0 0 24 24"><path fill="#0f9edc" d="M6.6 10.8c1.4 2.8 3.8 5.1 6.6 6.6l2.2-2.2c.3-.3.7-.4 1-.2 1.1.4 2.3.6 3.6.6.6 0 1 .4 1 1V20c0 .6-.4 1-1 1C10.6 21 3 13.4 3 4c0-.6.4-1 1-1h3.5c.6 0 1 .4 1 1 0 1.3.2 2.5.6 3.6.1.3 0 .7-.2 1z"/></svg>741.806.523</li>
    <li><svg width="16" height="12" viewBox="0 0 24 18"><rect x="1" y="1" width="22" height="16" rx="2" fill="#0f9edc"/><path d="M2 2l10 8 10-8" stroke="#24262d" stroke-width="2" fill="none"/></svg>info@laskowren.com</li>
  </ul>
  <ul class="abs footer-col" style="left:518px">
    <li><h4>FINANCE SERVICES</h4></li>
    <li>Equipment</li><li>Business</li><li>Commercial</li><li>Construction</li><li>Bridging</li>
  </ul>
  <ul class="abs footer-col" style="left:788px">
    <li><h4>COMPANY</h4></li>
    <li>About</li><li>Testimonials</li><li>Press</li>
  </ul>
  <ul class="abs footer-col" style="left:981px">
    <li><h4>SUPPORT</h4></li>
    <li>Contact</li><li>Community</li>
  </ul>
  <p class="abs copyright">© Peter Lasko-Wren Finance, Inc. <a href="#">Terms</a> <a href="#">Privacy Policy</a></p>
  <div class="abs socials footer-socials"><span></span><span></span><span></span><span></span><span></span></div>
</footer>

</body>
</html>
```